Graphic Design for a Info Card

We would like a graphic design for an info card . We would like the colours to correspond to our logo , you can add in the colours navy blue or yellow if you would like. We would like it to have the following information. We want something that really pops. We would like the size to be 4 1/2 x 6 .

ATTENTION!! Delivery Promo! Order from us on the @hopmorsel app or @vantrelcourier app on FRIDAYS and receive a FREE Sample of our one of our meal prep meals in your bag!
DID YOU KNOW?! Meal Prep is another great service that we offer. Saving you time, promoting your health, and best of all providing a delicious lunch . You can find more info on our website www.marlowpantry.example . All orders are available for delivery or pickup!

```html
<!DOCTYPE html>
<html lang="en">
<head>
<meta charset="utf-8">
<title>Marlow Pantry – Delivery Promo Card</title>
<link rel="stylesheet" href="https://fonts.googleapis.com/css2?family=Barlow+Condensed:wght@600;700&family=Barlow:wght@400;600;700&display=swap">
<style>
  :root {
    --green: #93c01f;
    --navy: #22304d;
    --yellow: #ffff00;
    --grey: #8e8e8e;
    --shadow: #cdcdcd;
    --white: #ffffff;
  }
  * { margin: 0; padding: 0; box-sizing: border-box; }
  html, body { width: 900px; height: 1200px; overflow: hidden; background: var(--white); }
  .card { position: relative; width: 900px; height: 1200px; background: var(--white); font-family: "Barlow", sans-serif; color: var(--navy); }

  .brand { position: absolute; left: 40px; top: 28px; }
  .brand-name { font-family: "Barlow", sans-serif; font-weight: 700; font-size: 58px; line-height: 1; color: var(--grey); letter-spacing: 1px; }
  .brand-tagline { margin-top: 8px; font-weight: 700; font-size: 23px; color: var(--green); letter-spacing: 0.3px; }

  .blob { position: absolute; left: 0; top: 0; width: 900px; height: 560px; }

  .headline { position: absolute; left: 0; width: 900px; text-align: center; font-family: "Barlow Condensed", sans-serif; font-weight: 700; color: var(--white); line-height: 1; }
  .headline-attention { top: 178px; font-size: 148px; letter-spacing: -1px; }
  .headline-promo { top: 322px; font-size: 104px; letter-spacing: -0.5px; }

  .offer { position: absolute; top: 546px; left: 0; width: 900px; text-align: center; font-size: 36px; line-height: 40px; }
  .offer strong { font-weight: 700; }
  .offer span { font-weight: 400; }

  .service { position: absolute; top: 720px; left: 0; width: 900px; height: 344px; background: linear-gradient(100deg, #2c3a4e 0%, #1b2536 45%, #18212f 70%, #3a3a2a 100%); }
  .service-title { position: absolute; top: 48px; width: 100%; text-align: center; font-family: "Barlow Condensed", sans-serif; font-weight: 700; font-size: 112px; line-height: 1; color: var(--yellow); }
  .service-lead { position: absolute; top: 166px; width: 100%; text-align: center; font-family: "Barlow Condensed", sans-serif; font-weight: 600; font-size: 42px; color: var(--white); }
  .benefits { position: absolute; top: 230px; left: 112px; display: flex; gap: 36px; list-style: none; }
  .benefit { display: flex; align-items: flex-start; gap: 8px; color: var(--white); font-weight: 700; font-size: 31px; line-height: 34px; }
  .benefit svg { width: 32px; height: 32px; flex: none; margin-top: 2px; }

  .info-pill { position: absolute; top: 1066px; left: 187px; width: 526px; height: 44px; background: var(--yellow); border-radius: 0 0 16px 16px; text-align: center; font-family: "Barlow Condensed", sans-serif; font-weight: 700; font-size: 33px; line-height: 44px; color: var(--navy); }
  .website { position: absolute; top: 1110px; width: 100%; text-align: center; font-weight: 700; font-size: 39px; line-height: 46px; color: var(--navy); }
  .footer { position: absolute; bottom: 0; left: 0; width: 900px; height: 39px; background: var(--navy); color: var(--white); text-align: center; font-weight: 700; font-size: 23px; line-height: 39px; }
</style>
</head>
<body>
<main class="card">
  <svg class="blob" viewBox="0 0 900 560" aria-hidden="true">
    <path fill="var(--shadow)" d="M0 193 C 60 158, 200 178, 330 168 C 450 158, 520 118, 660 130 C 780 138, 860 178, 900 213 L900 413 C 860 488, 800 538, 730 536 C 600 533, 500 488, 330 468 C 200 453, 60 458, 0 438 Z"/>
    <path fill="var(--green)" d="M0 175 C 60 140, 200 160, 330 150 C 450 140, 520 100, 660 112 C 780 120, 860 160, 900 195 L900 395 C 860 470, 800 520, 730 518 C 600 515, 500 470, 330 450 C 200 435, 60 440, 0 420 Z"/>
  </svg>

  <header class="brand">
    <div class="brand-name">MARLOW PANTRY</div>
    <div class="brand-tagline">HEALTHY KITCHEN &nbsp;|&nbsp; MEAL PREP</div>
  </header>

  <h1 class="headline headline-attention">ATTENTION!!</h1>
  <h2 class="headline headline-promo">DELIVERY PROMO!</h2>

  <p class="offer">
    <strong>Order from us on the @hopmorsel<br>app or @vantrelcourier app on FRIDAYS</strong><br>
    <span>Receive a FREE Sample of our one of our<br>meal prep meals in your bag!</span>
  </p>

  <section class="service" role="img" aria-label="Dark wooden table with fresh vegetables and fruit in a heart-shaped bowl">
    <h2 class="service-title">DID YOU KNOW?!</h2>
    <p class="service-lead">Meal Prep is another great service that we offer ;</p>
    <ul class="benefits">
      <li class="benefit">
        <svg viewBox="0 0 32 32"><circle cx="16" cy="16" r="15" fill="var(--yellow)"/><path d="M16 7 V16 H23" stroke="var(--navy)" stroke-width="3.5" fill="none" stroke-linecap="round"/></svg>
        <span>Saving<br>You time</span>
      </li>
      <li class="benefit">
        <svg viewBox="0 0 32 32"><path d="M16 29 L3 15 C-1 9, 4 2, 10 4 C13 5, 15 7, 16 9 C17 7, 19 5, 22 4 C28 2, 33 9, 29 15 Z" fill="var(--yellow)"/><path d="M4 15 H11 L13 11 L16 20 L19 13 L21 15 H28" stroke="var(--navy)" stroke-width="2.2" fill="none" stroke-linejoin="round"/></svg>
        <span>Promoting<br>Your health</span>
      </li>
      <li class="benefit">
        <svg viewBox="0 0 32 32" fill="var(--yellow)"><path d="M4 2 H6 V10 H8 V2 H10 V10 H12 V2 H14 V12 C14 15, 12 16, 11 16 V30 H7 V16 C6 16, 4 15, 4 12 Z"/><path d="M20 2 C26 2, 28 9, 27 16 H25 V30 H21 V16 C20 12, 19 6, 20 2 Z"/></svg>
        <span>Providing a<br>Delicious lunch</span>
      </li>
    </ul>
  </section>

  <div class="info-pill">Find More Info On Our Website</div>
  <p class="website">www.marlowpantry.example</p>
  <footer class="footer">*All orders are available for delivery or pickup!</footer>
</main>
</body>
</html>
```